Zerovan Medical

We are a medical supplier company we sell machines and equipment to all medical sectors in Iraq. Our services include not only the installation of these machines and equipment but also we provide support after installation and we train the staff to use these machines/equipment
We need a website that will make us stand out from our competitors, something professional and catchy
Starting from the home page, before showing the home page we want the loading screen to have our logo animated in a nice way
Then we can proceed to creating the other pages which are
Projects
Services
Training
About
and Contact us
Attached below is our logo and the color blue that we hope to use in the theme of the website
**** In the home page we want to focus on our partners and services****

Target Market(s)

Medical Sector

Industry/Entity Type

Medical

Coding

Coded - Design and coding required

Number of Pages Required

5+ page

Colors
0054AA
0677BA
7BADD7
CADEEF
E8F1F8

Requirements
Must have
• Animation in loading screen or animation in home page
Nice to have
• Some sort of animation for our partners

```html
<!DOCTYPE html>
<html lang="en">
<head>
<meta charset="utf-8">
<title>Zerovan Medical</title>
<link href="https://fonts.googleapis.com/css2?family=Poppins:wght@300;400;500;600&display=swap" rel="stylesheet">
<style>
:root{
  --blue:#0054AA;--blue2:#0677BA;--blue3:#7BADD7;--blue4:#CADEEF;--blue5:#E8F1F8;
  --ink:#1b1e2b;--muted:#6b7280;--white:#fff;--navy:#0b1f3f;--line:#e3e8ef;
}
*{box-sizing:border-box;margin:0;padding:0}
html,body{width:1200px;height:4815px;overflow:hidden}
body{font-family:'Poppins',sans-serif;color:var(--ink);background:#fff;position:relative}
.abs{position:absolute}
section,header,footer,.band{position:absolute;left:0;width:1200px}
.btn{position:absolute;background:var(--blue);color:#fff;border-radius:10px;font-weight:600;font-size:15px;display:flex;align-items:center;justify-content:center}
.btn-outline{background:transparent;border:1.5px solid #fff}
h2{font-weight:500;font-size:33px}
.ph{position:absolute}

.topbar{top:0;height:38px;background:var(--blue);color:#fff;font-size:12px}
.topbar .contact{position:absolute;left:113px;top:11px;display:flex;gap:26px}
.topbar .social{position:absolute;right:113px;top:10px;display:flex;gap:12px}
.dot{width:18px;height:18px;border-radius:50%;background:rgba(255,255,255,.9)}

.nav{top:38px;height:92px;background:#fff;border-bottom:1px solid var(--line)}
.brand{position:absolute;left:113px;top:30px;display:flex;align-items:center;gap:10px;font-weight:600;font-size:22px;color:var(--navy)}
.brand .mark{width:34px;height:34px;border:3px solid var(--blue);border-radius:4px}
.menu{position:absolute;left:414px;top:38px;display:flex;gap:30px;font-size:13px;color:#333}
.menu .on{color:var(--blue);font-weight:600;position:relative}
.menu .on::after{content:"";position:absolute;left:18px;top:40px;width:8px;height:8px;border-radius:50%;background:var(--blue)}

.hero{top:130px;height:625px;background:linear-gradient(90deg,#eef1f5,#e1e6ec 60%,#eef1f5)}
.hero .tag{position:absolute;left:113px;top:135px;background:var(--navy);color:#fff;font-size:40px;padding:2px 14px;border-radius:8px;font-weight:500}
.hero h1{position:absolute;left:113px;top:195px;font-size:58px;font-weight:500;line-height:68px;color:var(--navy)}
.hero p{position:absolute;left:113px;top:355px;width:520px;font-size:15px;line-height:23px}

.who{top:755px;height:495px;background:#f4f7fb}
.who h2{position:absolute;left:588px;top:133px}
.who p{position:absolute;left:588px;top:185px;width:470px;font-size:13px;line-height:20px;color:#555}

.stats{top:1250px;height:250px;background:var(--blue);color:#fff}
.stat{position:absolute;top:52px;width:230px}
.stat b{font-size:32px;font-weight:500;display:block}
.stat i{display:block;width:80px;height:1px;background:rgba(255,255,255,.5);margin:12px 0 18px}
.stat h4{font-size:17px;font-weight:500;margin-bottom:10px}
.stat p{font-size:12.5px;line-height:20px;opacity:.9}

.products{top:1500px;height:680px}
.pcard{position:absolute;left:113px;top:60px;width:314px;height:562px;background:linear-gradient(160deg,#0a5fb8,var(--blue));border-radius:12px;color:#fff;padding:40px 36px}
.pcard h3{font-size:34px;font-weight:500;line-height:42px}
.pcard p{font-size:12.5px;margin-top:14px;line-height:19px}
.item{position:absolute;width:206px;text-align:center;font-size:15px;font-weight:500}
.item .ph{position:relative;width:206px;height:204px;border-radius:10px;background:linear-gradient(160deg,var(--blue5),var(--blue4));margin-bottom:12px}
.arrow{position:absolute;width:32px;height:32px;border-radius:50%;display:flex;align-items:center;justify-content:center}

.services{top:2180px;height:545px;background:var(--blue)}
.services h2{color:#fff;text-align:center;margin-top:62px}
.scard{position:absolute;top:134px;width:232px;height:352px;background:#fff;border-radius:6px;text-align:center;padding:22px 16px}
.scard .ic{width:76px;height:76px;border-radius:50%;background:var(--blue5);margin:0 auto 18px;display:flex;align-items:center;justify-content:center}
.scard h4{font-size:17px;font-weight:500;line-height:23px;min-height:46px;display:flex;align-items:center;justify-content:center}
.scard p{font-size:12.5px;line-height:21px;color:#777;margin-top:10px;height:115px}
.scard .more{font-size:13px;margin-top:22px}

.partners{top:2725px;height:555px;overflow:hidden}
.partners h2{position:absolute;width:100%;text-align:center;top:72px}
.partners p{position:absolute;left:350px;width:500px;text-align:center;top:128px;font-size:13px;line-height:20px;color:#555}
.badge{position:absolute;border-radius:50%;background:#fff;box-shadow:0 4px 18px rgba(0,0,0,.1);display:flex;align-items:center;justify-content:center}
.badge span{display:block;border-radius:50%;background:var(--blue4)}

.why{top:3280px;height:370px}
.why h2,.clients h2{position:absolute;width:100%;text-align:center}
.why h2{top:36px}
.wcard{position:absolute;top:115px;width:232px;height:220px;border:1px solid var(--line);border-radius:6px;box-shadow:0 2px 10px rgba(0,0,0,.06);padding:26px 16px}
.wcard .ic{width:62px;height:62px;border-radius:50%;border:2px solid var(--blue3);display:flex;align-items:center;justify-content:center;margin-bottom:18px}
.wcard .ic b{width:44px;height:44px;border-radius:50%;background:var(--blue);display:block}
.wcard p{font-size:13.5px;line-height:20px}

.clients{top:3650px;height:350px}
.clients h2{top:35px}
.quote{position:absolute;left:260px;width:680px;top:125px;text-align:center;font-size:13px;line-height:20px;color:#666}
.stars{position:absolute;top:228px;width:100%;text-align:center;color:#f2c230;font-size:18px;letter-spacing:6px}
.who-said{position:absolute;top:260px;width:100%;text-align:center;font-size:18px;font-weight:500}

.contact{top:4000px;height:410px}
.contact h2{position:absolute;left:113px;top:120px;line-height:46px}
.contact p{position:absolute;left:113px;top:228px;width:360px;font-size:13px;line-height:21px;color:#555}

.footer{top:4410px;height:370px;background:var(--blue);color:#fff}
.form{position:absolute;left:650px;top:4025px;width:410px;height:405px;background:#fff;border-radius:12px;box-shadow:0 6px 24px rgba(0,0,0,.1);padding:30px 28px}
.form h3{text-align:center;font-size:24px;font-weight:500;margin-bottom:30px}
.field{background:#f1f3f6;border-radius:6px;height:55px;font-size:12px;color:#999;padding:17px 20px;margin-bottom:18px}
.row{display:flex;gap:16px}.row .field{flex:1}
.submit{background:var(--blue);color:#fff;border-radius:10px;height:53px;display:flex;align-items:center;justify-content:center;font-weight:600;font-size:15px}
.fcol{position:absolute;font-size:12.5px;line-height:19px}
.fcol h5{font-size:16px;font-weight:500;margin-bottom:16px}
.fcol .muted{opacity:.75}
.finfo{display:flex;gap:12px;margin-bottom:14px}
.news{position:absolute;left:776px;top:132px;width:291px;height:48px;background:#fff;border-radius:6px;font-size:12px;color:#999;padding:15px 16px}
.news b{position:absolute;right:8px;top:6px;width:36px;height:36px;border-radius:50%;background:var(--navy)}
.bottombar{top:4780px;height:35px;background:var(--navy);color:#cfd7e3;font-size:12px}
</style>
</head>
<body>

<header class="topbar">
  <div class="contact">
    <span>&#9990; +964 770 555 0142</span>
    <span>&#9993; hello@zerovanmedical.com</span>
  </div>
  <div class="social" aria-label="Social links"><i class="dot"></i><i class="dot"></i><i class="dot"></i></div>
</header>

<nav class="nav">
  <div class="brand"><span class="mark"></span>Zerovan Medical</div>
  <div class="menu"><span class="on">Home</span><span>About Us</span><span>Products</span><span>Services</span><span>Training</span><span>Partners</span></div>
  <div class="btn" style="left:938px;top:16px;width:152px;height:56px">Contact Us</div>
</nav>

<section class="hero">
  <div class="tag">Your Trusted Partner for</div>
  <h1>Advanced Medical<br>Solutions in Iraq</h1>
  <p>Providing high-quality medical equipment, expert installation, 24/7 support, and professional training to elevate healthcare standards.</p>
  <div class="btn" style="left:113px;top:433px;width:230px;height:56px">Explore Our Offerings</div>
  <svg class="ph" style="left:680px;top:120px" width="460" height="420" viewBox="0 0 460 420">
    <circle cx="233" cy="210" r="206" fill="none" stroke="var(--blue3)" stroke-dasharray="4 5"/>
    <circle cx="233" cy="210" r="196" fill="url(#hg)"/>
    <defs><linearGradient id="hg" x1="0" y1="0" x2="1" y2="1"><stop offset="0" stop-color="#7BADD7"/><stop offset="1" stop-color="#0677BA"/></linearGradient></defs>
  </svg>
  <div class="ph" role="img" aria-label="MRI scanner" style="left:640px;top:230px;width:420px;height:210px;border-radius:30px;background:linear-gradient(180deg,#f4f6f9,#d5dbe3)"></div>
</section>

<section class="who">
  <div class="ph" style="left:150px;top:53px;width:400px;height:400px;border:1.5px solid var(--blue3);border-radius:14px"></div>
  <div class="ph" role="img" aria-label="Operating room with surgical equipment" style="left:163px;top:62px;width:374px;height:380px;border-radius:12px;background:linear-gradient(160deg,#5f8fc8,#c9d7e6)"></div>
  <div class="ph" role="img" aria-label="Surgical team at work" style="left:95px;top:65px;width:178px;height:178px;border-radius:50%;border:4px solid #fff;background:linear-gradient(160deg,#3f74b5,#a7c2dd)"></div>
  <h2>Who We Are</h2>
  <p>We are a leading medical supplier in Iraq, committed to enhancing healthcare with innovative medical equipment and comprehensive services. With over a decade of experience, we provide complete solutions, from supply and installation to after sales support and staff training, ensuring your medical facilities operate seamlessly.</p>
  <div class="btn" style="left:588px;top:320px;width:148px;height:56px">Read More</div>
</section>

<section class="stats">
  <div class="stat" style="left:113px"><b>10+</b><i></i><h4>Years in Business</h4><p>Expertise in serving Iraq's healthcare sector.</p></div>
  <div class="stat" style="left:360px"><b>500+</b><i></i><h4>Installations</h4><p>successful installations across hospitals and clinics.</p></div>
  <div class="stat" style="left:610px"><b>50+</b><i></i><h4>Skilled Team</h4><p>A dedicated team professionals ready to assist you 24/7.</p></div>
  <div class="stat" style="left:857px"><b>200+</b><i></i><h4>Training Programs</h4><p>Empowered healthcare providers with specialized training.</p></div>
</section>

<section class="products">
  <div class="pcard">
    <h3>Our Medical Equipment Products</h3>
    <p>Delivering Quality, Precision, and Innovation</p>
    <div class="btn btn-outline" style="left:36px;top:480px;width:182px;height:56px;font-size:14px">More Category</div>
  </div>
  <div class="item" style="left:443px;top:61px"><div class="ph" role="img" aria-label="ICU bed equipment"></div>I.C.U Bed Electric</div>
  <div class="item" style="left:664px;top:61px"><div class="ph" role="img" aria-label="Anesthesia equipment"></div>Anesthesia Equipment</div>
  <div class="item" style="left:884px;top:61px"><div class="ph" role="img" aria-label="C-arm unit"></div>C-Arm I.C.U Bed</div>
  <div class="item" style="left:443px;top:320px"><div class="ph" role="img" aria-label="Angio bed"></div>Angio Electric Bed</div>
  <div class="item" style="left:664px;top:320px"><div class="ph" role="img" aria-label="Radiosurgery system"></div>Radiosurgery Treatment</div>
  <div class="item" style="left:884px;top:320px"><div class="ph" role="img" aria-label="Digital thermometer"></div>Digital thermometer</div>
  <div class="arrow" style="left:1003px;top:588px;border:1px solid var(--blue4);color:var(--blue)">&#8249;</div>
  <div class="arrow" style="left:1056px;top:588px;background:var(--blue);color:#fff">&#8250;</div>
</section>

<section class="services">
  <h2>Our Comprehensive Services</h2>
  <div class="scard" style="left:113px"><div class="ic"><svg width="34" height="34" viewBox="0 0 24 24" fill="none" stroke="var(--blue)" stroke-width="2"><path d="M2 4h3l3 11h11l2-8H6"/><circle cx="9" cy="19" r="1.5"/><circle cx="17" cy="19" r="1.5"/></svg></div><h4>Medical Equipment Supply</h4><p>We provide a diverse range of top-quality medical machines tailored to meet the specific needs of healthcare facilities across Iraq.</p><div class="more">Read More &#9656;</div></div>
  <div class="scard" style="left:360px"><div class="ic"><svg width="34" height="34" viewBox="0 0 24 24" fill="none" stroke="var(--blue)" stroke-width="2.2"><path d="M4 20l9-9M14 4l6 6-3 3-6-6zM4 4l16 16"/></svg></div><h4>Installation &amp; Setup</h4><p>Our expert team handles complete installation and setup of medical equipment, ensuring your facility is ready to operate efficiently from day one.</p><div class="more">Read More &#9656;</div></div>
  <div class="scard" style="left:608px"><div class="ic"><svg width="34" height="34" viewBox="0 0 24 24" fill="none" stroke="var(--blue)" stroke-width="2"><circle cx="15" cy="8" r="4"/><path d="M2 18h5l4 2 8-4"/></svg></div><h4>Technical Support &amp; Maintenance</h4><p>We offer round-the-clock technical support and regular maintenance services to keep your equipment running at its best.</p><div class="more">Read More &#9656;</div></div>
  <div class="scard" style="left:856px"><div class="ic"><svg width="34" height="34" viewBox="0 0 24 24" fill="none" stroke="var(--blue)" stroke-width="2"><rect x="3" y="4" width="18" height="11"/><circle cx="8" cy="19" r="2"/><circle cx="16" cy="19" r="2"/></svg></div><h4>Professional Training Programs</h4><p>Customized training sessions for your staff to effectively operate and maintain the latest medical technology.</p><div class="more">Read More &#9656;</div></div>
</section>

<section class="partners">
  <svg class="ph" style="left:0;top:0" width="1200" height="555" viewBox="0 0 1200 555">
    <circle cx="600" cy="-140" r="600" fill="var(--blue5)"/>
    <circle cx="600" cy="-140" r="610" fill="none" stroke="#cbd2dc" stroke-dasharray="3 6"/>
  </svg>
  <h2>Our Trusted Partners</h2>
  <p>We collaborate with renowned global manufacturers to deliver the most reliable medical equipment to our clients.</p>
  <div class="btn" style="left:527px;top:180px;width:146px;height:52px">Read More</div>
  <div class="badge" role="img" aria-label="Partner badge" style="left:45px;top:35px;width:106px;height:106px"><span style="width:70px;height:24px;border-radius:12px"></span></div>
  <div class="badge" role="img" aria-label="Partner badge" style="left:1050px;top:35px;width:106px;height:106px"><span style="width:58px;height:58px"></span></div>
  <div class="badge" role="img" aria-label="Partner badge" style="left:222px;top:272px;width:106px;height:106px"><span style="width:54px;height:54px"></span></div>
  <div class="badge" role="img" aria-label="Partner badge" style="left:870px;top:272px;width:106px;height:106px"><span style="width:54px;height:54px"></span></div>
  <div class="badge" role="img" aria-label="Partner badge" style="left:530px;top:380px;width:134px;height:134px"><span style="width:86px;height:40px;border-radius:20px"></span></div>
</section>

<section class="why">
  <h2>Why Choose Us</h2>
  <div class="wcard" style="left:113px"><div class="ic"><b></b></div><p>Over a decade of experience in the medical supply industry</p></div>
  <div class="wcard" style="left:360px"><div class="ic"><b></b></div><p>Comprehensive 24/7 customer support for all technical needs.</p></div>
  <div class="wcard" style="left:608px"><div class="ic"><b></b></div><p>Customizable solutions to fit your facility's unique requirements</p></div>
  <div class="wcard" style="left:856px"><div class="ic"><b></b></div><p>A strong network of global partners ensures high-quality equipment</p></div>
</section>

<section class="clients">
  <h2>What Our Clients Say</h2>
  <div class="arrow" style="left:190px;top:130px;background:var(--blue);color:#fff">&#8249;</div>
  <div class="arrow" style="left:988px;top:130px;background:var(--blue);color:#fff">&#8250;</div>
  <p class="quote">"Lorem ipsum dolor sit amet, consectetur adipiscing elit, sed do eiusmod tempor incididunt ut labore et dolore magna aliqua. Ut enim ad minim veniam, quis nostrud exercitation ullamco laboris nisi ut aliquip ex ea commodo consequat"</p>
  <div class="stars">&#9733;&#9733;&#9733;&#9733;<span style="color:#ddd">&#9733;</span></div>
  <div class="who-said">Nadia Karim</div>
  <div class="ph" style="left:512px;top:314px;width:176px;height:2px;background:var(--line)"></div>
  <div class="ph" style="left:512px;top:313px;width:44px;height:4px;background:var(--blue)"></div>
</section>

<section class="contact">
  <h2>Ready to Elevate Your<br>Healthcare Facility</h2>
  <p>Contact us today to learn more about our medical equipment, services, and training programs. Our team is here to assist you with all your needs</p>
</section>

<footer class="footer">
  <div class="ph" style="left:113px;top:65px;width:84px;height:66px;border:3px solid #fff;border-radius:4px"></div>
  <div class="fcol" style="left:113px;top:210px"><h5 style="font-size:15px;margin-bottom:14px">Follow Us on</h5><div style="display:flex;gap:12px"><i class="dot"></i><i class="dot"></i><i class="dot"></i></div></div>
  <div class="fcol" style="left:330px;top:72px;width:230px">
    <h5>Contact Info</h5>
    <div class="finfo"><span>&#9990;</span><div>Phone<br><span class="muted">+964 770 555 0142</span></div></div>
    <div class="finfo"><span>&#9993;</span><div>Email<br><span class="muted">hello@zerovanmedical.com</span></div></div>
    <div class="finfo"><span>&#9906;</span><div>Address<br><span class="muted">14 Karrada Street<br>Baghdad, IQ</span></div></div>
  </div>
  <div class="fcol" style="left:600px;top:72px;line-height:28.5px">
    <h5 style="margin-bottom:8px">Quick Links</h5>
    <div class="muted">Home<br>About Us<br>Products<br>Services<br>Training<br>Partners</div>
  </div>
  <div class="fcol" style="left:776px;top:72px"><h5>Subscribe to our Newsletter!</h5></div>
  <div class="news">Email Address<b></b></div>
</footer>

<div class="form">
  <h3>Get In Touch With Us</h3>
  <div class="row"><div class="field">Your name</div><div class="field">Last Name</div></div>
  <div class="row"><div class="field">Phone number</div><div class="field">Email Address</div></div>
  <div class="field" style="height:90px">Message</div>
  <div class="submit">Submit</div>
</div>

<div class="band bottombar">
  <span class="abs" style="left:133px;top:10px">© 2024 Zerovan Medical. All rights reserved.</span>
  <span class="abs" style="left:692px;top:10px">Terms and Conditions</span>
  <span class="abs" style="left:872px;top:10px">Privacy Policy</span>
  <span class="abs" style="left:996px;top:10px">Disclaimer</span>
</div>

</body>
</html>
```